Educational Construction Organization needs Flyer for Upcoming Forum

We need a SAVE THE DATE Flyer for our 2020 Ravteq Forum. We work with Architects, Engineers, Contractors and Owners in the design and construction industry. Our mission is to evolve the capital projects industry through sharing of knowledge for optimized leadership, delivery and performance. The final design should communicate the connection between these industry professionals, our mission, and the Forum theme and byline.
Updates

Need extra days to review

Target Market(s)

Design and construction industry.

Industry/Entity Type

Construction

Font styles to use
Sans Serif

Colors

Designer to choose colors to be used in the design.

Requirements
Must have
• Title, By-line, 3 key topics, Date and location. Design that implements the theme with graphic(s) (not just text).
• NEW TITLE: FUTURE PROOFING: Connecting the dots to make sense of the "SMART" City
• 3 Key Topics: Smart Cities, Smart Institutions, Smart Connections
• Date: April 1-3, 2020
• Location: San Antonio, TX
Nice to have
• Please review attached problem statement for a better understanding of what this Forum will focus on when designing your graphic for the flyer.

```html
<!DOCTYPE html>
<html lang="en">
<head>
<meta charset="utf-8">
<title>2020 Ravteq Forum – Future Proofing: Making Sense of the Smart City</title>
<link href="https://fonts.googleapis.com/css2?family=Roboto:wght@300;400;500;700;900&family=Montserrat:wght@700;800&display=swap" rel="stylesheet">
<style>
:root{
  --white:#ffffff;
  --paper:#eeeeee;
  --charcoal:#3b3b3d;
  --bar:#444447;
  --navy:#0d1733;
  --navy-deep:#0a1128;
  --green:#8dc63f;
  --cyan:#3ab0e6;
  --blue:#1f5fbf;
  --panel:rgba(40,40,44,.84);
}
*{margin:0;padding:0;box-sizing:border-box}
html,body{width:850px;height:1200px;overflow:hidden;background:var(--paper)}
.flyer{position:relative;width:850px;height:1200px;background:var(--paper);font-family:"Roboto",Arial,sans-serif;color:var(--white);overflow:hidden}

/* header */
.header{position:absolute;left:0;top:0;width:850px;height:147px;background:var(--white)}
.brand{position:absolute;left:44px;top:32px;display:flex;align-items:center;gap:14px}
.brand-dot{width:74px;height:74px;border-radius:50%;background:var(--blue)}
.brand-name{font-weight:700;font-size:46px;color:#4a4a4a;line-height:1}
.forum-bar{position:absolute;left:306px;top:111px;width:544px;height:36px;background:var(--bar);color:var(--white);font-size:21px;font-weight:500;line-height:36px;padding-left:26px}

/* hero */
.hero{position:absolute;left:0;top:147px;width:850px;height:472px;
  background:
    linear-gradient(168deg,transparent 62%,rgba(255,120,200,.35) 66%,transparent 70%),
    linear-gradient(172deg,transparent 70%,rgba(120,200,255,.45) 73%,transparent 77%),
    linear-gradient(176deg,transparent 78%,rgba(255,170,90,.35) 81%,transparent 85%),
    radial-gradient(ellipse at 22% 48%,rgba(120,190,255,.75) 0%,transparent 38%),
    radial-gradient(ellipse at 48% 30%,rgba(70,140,230,.55) 0%,transparent 35%),
    radial-gradient(ellipse at 75% 85%,#7a2f78 0%,transparent 45%),
    linear-gradient(180deg,#0a1836 0%,#143a78 42%,#27498a 66%,#1c1f44 100%)}
.web-tag{position:absolute;left:0;top:147px;width:364px;height:42px;background:var(--green);clip-path:polygon(0 0,100% 0,92% 100%,0 100%);display:flex;align-items:center;gap:10px;padding-left:28px;font-size:18px;font-weight:500}
.web-tag svg{width:20px;height:20px}
.title-panel{position:absolute;left:430px;top:263px;width:390px;height:356px;background:var(--panel)}
.title-kicker{position:absolute;left:470px;top:282px;font-weight:900;font-size:22px;letter-spacing:2px;color:var(--green);line-height:1}
.title-byline{position:absolute;left:470px;top:311px;font-weight:500;font-size:14px;letter-spacing:1.5px;color:#dfe6f2;line-height:1}
.title-main{position:absolute;left:468px;top:340px;font-weight:900;font-size:82px;line-height:.9;letter-spacing:1px}
.title-sub{position:absolute;left:470px;top:500px;font-weight:700;font-size:45px;line-height:1.3}
.date-year{position:absolute;left:179px;top:508px;width:124px;height:44px;line-height:44px;transform:rotate(-90deg);text-align:center;font-size:42px;font-weight:300;letter-spacing:1px}
.date-days{position:absolute;left:270px;top:458px;font-size:104px;font-weight:900;line-height:1}
.date-month{position:absolute;left:280px;top:552px;font-size:50px;font-weight:300;line-height:1}

/* left column */
.intro{position:absolute;left:0;top:619px;width:430px;height:581px;background:var(--charcoal)}
.topics{position:absolute;left:34px;top:644px;display:flex}
.topic{width:116px;text-align:center;font-size:13px;font-weight:700;line-height:1.25}
.topic+.topic{border-left:2px solid #d0d0d0;margin-left:8px;padding-left:8px}
.topic svg{width:48px;height:48px;display:block;margin:0 auto 12px}
.intro-copy{position:absolute;left:26px;top:772px;width:390px;font-size:11.4px;line-height:1.52;color:#f2f2f2}
.intro-copy p+p{margin-top:18px}
.location-accent{position:absolute;left:0;top:1047px;width:58px;height:78px;background:var(--green)}
.location{position:absolute;left:58px;top:1047px;width:372px;height:92px;background:var(--navy);display:flex;align-items:center;gap:12px;padding-left:22px;font-family:"Montserrat",Arial,sans-serif;font-weight:800;font-size:28px;letter-spacing:.5px}
.location svg{width:26px;height:30px}

/* right column */
.vision-art{position:absolute;left:430px;top:619px;width:396px;height:206px;
  background:
    radial-gradient(circle at 38% 55%,#c8f0ff 0%,#5ab8f0 12%,#1f5fbf 32%,transparent 55%),
    radial-gradient(ellipse at 88% 50%,rgba(220,220,235,.55) 0%,transparent 22%),
    radial-gradient(ellipse at 20% 20%,rgba(90,160,230,.35) 0%,transparent 40%),
    linear-gradient(135deg,#0b1a3c 0%,#0a1430 100%)}
.vision{position:absolute;left:430px;top:825px;width:396px;height:375px;background:var(--navy-deep)}
.vision-head{position:absolute;left:448px;top:840px;display:flex;align-items:center;gap:10px;font-family:"Montserrat",Arial,sans-serif;font-weight:800;font-size:24px}
.vision-head svg{width:30px;height:20px}
.vision-copy{position:absolute;left:442px;top:890px;width:374px;font-size:11.4px;line-height:1.5;color:#eaeaea}
</style>
</head>
<body>
<div class="flyer">
  <header class="header">
    <div class="brand"><span class="brand-dot"></span><span class="brand-name">Ravteq</span></div>
    <div class="forum-bar">2020 Ravteq Forum</div>
  </header>

  <div class="hero" role="img" aria-label="Night-time city skyline with glowing skyscrapers and streaking light trails"></div>
  <div class="web-tag">
    <svg viewBox="0 0 20 20"><circle cx="10" cy="10" r="8.5" fill="none" stroke="#fff" stroke-width="1.6"/><path d="M1.5 10h17M10 1.5c-4 4.5-4 12.5 0 17M10 1.5c4 4.5 4 12.5 0 17" fill="none" stroke="#fff" stroke-width="1.4"/></svg>
    ravteq-forum.org
  </div>
  <div class="title-panel"></div>
  <p class="title-kicker">FUTURE PROOFING:</p>
  <p class="title-byline">CONNECTING THE DOTS TO</p>
  <h1 class="title-main">MAKING<br>SENSE</h1>
  <p class="title-sub">OF THE<br>“SMART” CITY</p>
  <div class="date-year">2020</div>
  <div class="date-days">1-3</div>
  <div class="date-month">APRIL</div>

  <section class="intro"></section>
  <div class="topics">
    <div class="topic">
      <svg viewBox="0 0 48 48" fill="none" stroke="#3ab0e6" stroke-width="3"><rect x="8" y="18" width="10" height="24"/><rect x="20" y="8" width="10" height="34"/><rect x="32" y="22" width="9" height="20"/></svg>
      SMART<br>CITIES
    </div>
    <div class="topic">
      <svg viewBox="0 0 48 48" fill="#3ab0e6"><circle cx="24" cy="24" r="8"/><circle cx="10" cy="12" r="5"/><circle cx="38" cy="12" r="5"/><circle cx="10" cy="36" r="5"/><circle cx="38" cy="36" r="5"/></svg>
      SMART<br>INSTITUTIONS
    </div>
    <div class="topic">
      <svg viewBox="0 0 48 48" fill="#3ab0e6" stroke="#3ab0e6" stroke-width="2.5"><path d="M24 24L10 10M24 24L40 12M24 24L12 40M24 24L38 38"/><circle cx="24" cy="24" r="7"/><circle cx="10" cy="10" r="4"/><circle cx="40" cy="12" r="4"/><circle cx="12" cy="40" r="4"/><circle cx="38" cy="38" r="4"/></svg>
      SMART<br>CONNECTIONS
    </div>
  </div>
  <div class="intro-copy">
    <p>All over the nation, regions, cities and facility Owners are trying to get a handle on being “smart.” What does that mean for their piece of the built environment? Why should they care? Is it too late for them to get on board? Is this a justifiable investment or a waste of time, money and effort? Is being “smart” only focused on technologies? Who is coordinating all this stuff? Are cross-connections being made?</p>
    <p>It is obvious that a city provides different value to different stakeholders – depending on their needs in the moment – whether they are facility operators or planners, and whether or not that city is “smart,” at some point we all become end-users. We may not even consider our facilities or city as “smart,” but we experience them as places in which we work, play, live, visit.</p>
  </div>
  <div class="location-accent"></div>
  <div class="location">
    <svg viewBox="0 0 26 30"><path d="M13 2a10 10 0 0 0-10 10c0 7 10 16 10 16s10-9 10-16A10 10 0 0 0 13 2z" fill="none" stroke="#fff" stroke-width="2.4"/><circle cx="13" cy="12" r="3.6" fill="#fff"/></svg>
    SAN ANTONIO, TX
  </div>

  <div class="vision-art" role="img" aria-label="Glowing digital globe of connected data points beside a reaching hand"></div>
  <section class="vision"></section>
  <h2 class="vision-head">
    <svg viewBox="0 0 30 20"><path d="M1 10C6 2 24 2 29 10 24 18 6 18 1 10z" fill="none" stroke="#fff" stroke-width="2.2"/><circle cx="15" cy="10" r="4.5" fill="#fff"/></svg>
    OUR VISION
  </h2>
  <div class="vision-copy">
    <p>The Global Society of Urban Engineers (GSUE) envisions a smart city as one that brings together technology, government, and society to enable the following characteristics: a smart economy, smart mobility, a smart environment, smart people, smart living, smart governance.</p>
    <p>In my mind, being a “smart city” encompasses a lot of things – incorporating technology, yes, but also with an eye on cultural and aspects. At the end of the day, we all want to work, live, play and visit places that are safe, beautiful and clean, (maybe even exciting and invigorating), and we want to get stuff done expediently and with less stress. Being “smart” is a tool to help accomplish these goals. And, being smart means connecting the dots to bring out the best of all these facets!</p>
  </div>
</div>
</body>
</html>
```